Your Ridgeview Homefinder Website Design

Creative Brief: Website Design for Your Ridgeview Homefinder
- Project Overview: Design a website for our new brand, "Your Ridgeview Homefinder". Your Ridgeview Homefinder is a service that matches clients with the perfect realtor. The primary function of this site is to serve as a lead generation hub, to generate leads of people who are looking to either buy or sell their house and need a great realtor. The site needs to have a very clean, modern design using sites like Quillmark, Lumhaven, Trevista, and Pravlo as an example. The site also needs to have a primary lead capture capability through a multi-step form or questionnaire that indicates if they are buying or selling, and depending on that selection, creates two different flows.

Target Audience:
- Homebuyers and sellers in the Denver area
- Individuals looking for high-quality realtor services
- Users seeking a seamless and professional online & home buying/selling experience

Objectives:
- Create a visually appealing, modern website with a strong emphasis on lead generation.
- Design advanced, multi-step forms for efficient lead capture.
- Ensure the website is user-friendly and optimized for both desktop and mobile devices.

Pages to Design:
Home Page:
- Engaging hero section with a clear call to action and the ability to enter the form flow
- Brief introduction to Your Ridgeview Homefinder and its unique value proposition
- Key features & benefits of being matched with a realtor by Your Ridgeview Homefinder
- Testimonials and success stories
- Lead capture form

About Page:
- Overview of Your Ridgeview Homefinder’s mission and values
- Professional and trust-building imagery

How it Works Page:
- Step-by-step explanation of the matching process (complete the form and we will match you with a realtor)
- Visual aids (icons, graphics) to simplify complex information
- Customer journey map from inquiry to successful match & sale of home
- Lead capture form

Contact Us Page:
- Simple and accessible contact form
- Contact details
- Call to action for immediate inquiries

Blog Template:
- Clean, easy-to-read layout for blog posts, primarily location/neighborhood guides as well as standard blogs
- Sidebar for recent posts, categories, and tags
- Social sharing buttons
- Lead capture form embedded within blog posts

Design Style:
- Modern and professional with a focus on usability
- Clean lines and intuitive navigation
- Use of curved corners and minimal straight lines for a sleek look
- Incorporation of graphic design elements, potentially including 3D and isomorphic design
- Inspired by sites like Quillmark, Lumhaven, Trevista, and Pravlo
Consistent color scheme and typography

Visual References:
- Quillmark: For its professional and corporate look
- Lumhaven and Trevista: For their user-friendly interfaces and modern design
- Pravlo: For its clean and functional layout

Target Market(s)

- Homebuyers and sellers in the Denver area, Individuals looking for high-quality realtor services, Users seeking a seamless and professional home buying/selling experience

Industry/Entity Type

Real Estate

Number of Pages Required

5+ page

Requirements
Must have
• Fully designed website with lead capture functionality based on brief
Nice to have
• Designed in Figma, Starting / Placeholder copy

```html
<!DOCTYPE html>
<html lang="en">
<head>
<meta charset="utf-8">
<title>Ridgeview Homefinder</title>
<link href="https://fonts.googleapis.com/css2?family=Poppins:wght@400;500;600;700&display=swap" rel="stylesheet">
<style>
:root{
  --orange:#ef7d00;
  --orange-light:#f6a623;
  --grad:linear-gradient(180deg,#f7a520,#e86e00);
  --ink:#111111;
  --body:#555555;
  --soft:#f5f5f5;
  --line:#cfcfcf;
  --footer:#0e0e0e;
}
*{box-sizing:border-box;margin:0;padding:0}
html,body{width:1200px;height:4525px;overflow:hidden;background:#fff;font-family:'Poppins',sans-serif;color:var(--ink)}
.page{position:relative;width:1200px;height:4525px}
.abs{position:absolute}
.accent{color:var(--orange)}
.btn{position:absolute;display:flex;align-items:center;justify-content:center;background:var(--grad);color:#fff;font-weight:600;border-radius:30px;box-shadow:0 4px 10px rgba(232,110,0,.3)}
.section-title{position:absolute;left:0;width:1200px;text-align:center;font-size:31px;font-weight:700}
.section-title::after{content:"";display:block;width:48px;height:3px;background:var(--orange);margin:10px auto 0;border-radius:2px}

/* header */
.brand{position:absolute;left:100px;top:20px;display:flex;align-items:center;gap:12px}
.brand-dot{width:56px;height:56px;border:4px solid var(--orange);border-radius:50%}
.brand-name{font-size:26px;font-weight:600;line-height:1.1;color:var(--ink)}
.topbar{position:absolute;left:450px;top:0;width:750px;height:50px;background:var(--grad);border-bottom-left-radius:26px;display:flex;align-items:center;padding-left:72px;gap:26px;color:#fff;font-size:16px}
.topbar .item{display:flex;align-items:center;gap:12px}
.topbar .ic{width:32px;height:32px;border:2px solid #fff;border-radius:50%;display:flex;align-items:center;justify-content:center}
.social{display:flex;gap:7px}
.social span{width:26px;height:26px;border:2px solid #fff;border-radius:50%}
.nav{position:absolute;top:62px;left:552px;display:flex;gap:50px;font-size:15px}
.nav a{color:var(--ink);text-decoration:none}
.nav a.active{color:var(--orange);font-weight:600;border-bottom:2px solid var(--orange);padding-bottom:2px}

/* hero */
.hero-title{position:absolute;left:100px;top:178px;width:420px;font-size:50px;font-weight:700;line-height:1.15}
.hero-text{position:absolute;left:100px;top:360px;width:420px;font-size:14px;line-height:1.9;color:#333}
.dots{position:absolute;left:103px;top:528px;display:flex;gap:8px;align-items:center}
.dots span{width:9px;height:9px;border-radius:50%;background:#bbb}
.dots span:first-child{width:12px;height:12px;background:var(--orange-light)}
.hero-art{position:absolute;left:545px;top:118px;width:655px;height:410px;border-radius:180px 40px 200px 160px;background:radial-gradient(circle at 60% 55%,#d9e2f2 0%,#e7ecf6 50%,#fbefe0 100%)}

/* features */
.features{position:absolute;left:0;top:635px;width:1200px;height:692px;background:var(--soft)}
.card{position:absolute;background:#fff;border-radius:12px;box-shadow:0 4px 18px rgba(0,0,0,.08);text-align:center}
.f-card{top:168px;width:302px;height:352px;padding:0 22px}
.f-icon{width:94px;height:94px;border-radius:50%;margin:28px auto 0;background:#fff;box-shadow:6px 0 0 #fbe5d3,0 2px 10px rgba(0,0,0,.1)}
.f-card h3{font-size:16px;font-weight:600;margin-top:24px}
.f-card p{font-size:14px;line-height:2.05;color:var(--body);margin-top:8px}
.f-card .btn{position:relative;width:116px;height:38px;margin:12px auto 0;font-size:13px}
.arrow{position:absolute;width:26px;height:26px;border:1.5px solid #555;border-radius:50%;display:flex;align-items:center;justify-content:center}
.outline-btn{position:absolute;left:532px;top:570px;width:136px;height:50px;border:2px solid var(--orange);border-radius:30px;display:flex;align-items:center;justify-content:center;color:var(--orange);font-weight:600;font-size:16px}

/* about */
.about-text{position:absolute;left:140px;top:1460px;width:920px;text-align:center;font-size:14px;line-height:2.1;color:var(--body)}
.about-head{position:absolute;left:98px;top:1612px;font-size:25px;font-weight:500;line-height:1.6}
.values{position:absolute;left:98px;top:1712px;list-style:none;width:420px}
.values li{position:relative;padding-left:34px;font-size:15px;line-height:1.95;color:#444;margin-bottom:17px}
.values li::before{content:"";position:absolute;left:0;top:6px;width:18px;height:18px;border:2px solid var(--orange-light);border-radius:50%}
.about-art{position:absolute;left:615px;top:1580px;width:460px;height:470px;border-radius:50%;background:radial-gradient(circle at 50% 50%,#ffffff 0%,#fdf1e3 45%,#fbe2c6 100%)}

/* testimonials */
.testi{position:absolute;left:0;top:2140px;width:1200px;height:575px;background:var(--soft)}
.t-card{top:152px;width:310px;height:330px;text-align:left;padding:28px 26px}
.stars{color:var(--orange);font-size:15px;letter-spacing:2px}
.t-card p{font-size:13.5px;line-height:1.9;color:#333;margin-top:8px}
.t-card hr{border:none;border-top:1px solid #ccc;margin:28px 0 26px}
.person{display:flex;gap:18px;align-items:center}
.avatar{width:56px;height:56px;border-radius:50%;background:#c9b8a8}
.person b{font-size:17px;font-weight:600;display:block}
.person span{font-size:14px;color:#444}

/* contact */
.step{position:absolute;top:2886px;width:60px;height:60px;border-radius:50%;display:flex;align-items:center;justify-content:center;font-size:28px;font-weight:500}
.step.out{border:2px solid var(--orange);color:var(--orange);background:#fff}
.step.fill{background:var(--grad);color:#fff}
.step-line{position:absolute;top:2915px;height:2px;background:#999}
.field{position:absolute;height:45px;border:1px solid #c8c8c8;font-size:13px;color:#666;padding:13px 20px 0}
.full{left:160px;width:882px}
.l{left:160px;width:426px}
.r{left:615px;width:427px}
.divider{position:absolute;left:160px;width:880px;height:3px;background:#bbb}
.q{position:absolute;left:160px;top:3578px;font-size:13px;color:#555}
.radios{position:absolute;left:160px;top:3614px;display:flex;gap:30px;font-size:13px;color:#555}
.radios label{display:flex;align-items:center;gap:10px}
.radios i{width:26px;height:26px;border:1px solid #bbb;border-radius:50%}

/* footer */
.footer{position:absolute;left:0;top:4080px;width:1200px;height:445px;background:var(--footer);color:#fff}
.footer h4{position:absolute;font-size:20px;font-weight:500}
.footer h4::after{content:"";display:block;width:38px;height:2px;background:var(--orange);margin-top:8px}
.f-list{position:absolute;list-style:none;font-size:14px;line-height:2.1}
.f-small{position:absolute;font-size:14px;line-height:1.6}
.f-social{position:absolute;left:118px;top:225px;display:flex;gap:10px}
.f-social span{width:40px;height:40px;border:2px solid #fff;border-radius:50%}
.email-box{position:absolute;left:852px;top:202px;width:237px;height:38px;background:#fff;border-radius:20px;color:#333;font-size:13px;padding:9px 20px}
.email-box span{position:absolute;right:12px;top:11px;width:16px;height:16px;border-radius:50%;background:var(--orange)}
.copy{position:absolute;left:110px;top:375px;width:980px;border-top:1px solid #555;text-align:center;font-size:15px;padding-top:22px}
</style>
</head>
<body>
<div class="page">

  <header>
    <div class="brand"><span class="brand-dot"></span><span class="brand-name">Ridgeview<br><span class="accent" style="font-size:16px;letter-spacing:4px">Homefinder</span></span></div>
    <div class="topbar">
      <div class="item"><span class="ic"><svg width="14" height="14" viewBox="0 0 24 24"><path fill="#fff" d="M6.6 10.8a15.1 15.1 0 0 0 6.6 6.6l2.2-2.2a1 1 0 0 1 1-.25 11.4 11.4 0 0 0 3.6.57 1 1 0 0 1 1 1V20a1 1 0 0 1-1 1A17 17 0 0 1 3 4a1 1 0 0 1 1-1h3.5a1 1 0 0 1 1 1c0 1.25.2 2.45.57 3.6a1 1 0 0 1-.25 1z"/></svg></span>+1 555 010 2040</div>
      <div class="item"><span class="ic"><svg width="14" height="12" viewBox="0 0 24 18"><path fill="#fff" d="M0 0h24v18H0z"/><path d="M2 2l10 7 10-7" stroke="#ee8200" stroke-width="2" fill="none"/></svg></span>info@ridgeviewhome.com</div>
      <div class="social" aria-label="Social links"><span></span><span></span><span></span></div>
    </div>
    <nav class="nav"><a class="active">Home</a><a>About Us</a><a>How it Works</a><a>Blog</a><a>Contact Us</a></nav>
  </header>

  <section class="hero">
    <h1 class="hero-title"><span class="accent">WELCOME</span> To<br>Ridgeview<br><span class="accent">Homefinder</span></h1>
    <p class="hero-text">Lorem ipsum dolor sit amet, consectetur adipiscing eiusmod tempor incididunt ut labore et dolore magna aliqua.</p>
    <div class="btn" style="left:100px;top:444px;width:145px;height:47px;font-size:16px">Get Started</div>
    <div class="dots"><span></span><span></span><span></span><svg style="margin-left:40px" width="44" height="8"><line x1="0" y1="4" x2="16" y2="4" stroke="#bbb"/><line x1="24" y1="4" x2="42" y2="4" stroke="#111" stroke-width="2"/><path d="M38 1l4 3-4 3" stroke="#111" fill="none"/></svg></div>
    <div class="hero-art" role="img" aria-label="Illustration of two people discussing a house purchase beside a red house, dollar and percent signs"></div>
  </section>

  <section class="features">
    <h2 class="section-title" style="top:74px"><span class="accent">Key Features</span> &amp; Benefits</h2>
    <div class="card f-card" style="left:100px"><div class="f-icon" role="img" aria-label="Agent icon"></div><h3>Lorem ipsum dolor</h3><p>Sed ut perspiciatis unde omnis iste totam rem aperiam, eaque ipsa quae beatae vitae dicta sunt explicabo.</p><div class="btn">Read More</div></div>
    <div class="card f-card" style="left:450px"><div class="f-icon" role="img" aria-label="Realtor profiles icon"></div><h3>Lorem ipsum dolor</h3><p>Sed ut perspiciatis unde omnis iste totam rem aperiam, eaque ipsa quae beatae vitae dicta sunt explicabo.</p><div class="btn">Read More</div></div>
    <div class="card f-card" style="left:800px"><div class="f-icon" role="img" aria-label="Building and badge icon"></div><h3>Lorem ipsum dolor</h3><p>Sed ut perspiciatis unde omnis iste totam rem aperiam, eaque ipsa quae beatae vitae dicta sunt explicabo.</p><div class="btn">Read More</div></div>
    <div class="arrow" style="left:38px;top:331px;border-color:#aaa"><svg width="8" height="10"><path d="M6 1L2 5l4 4" stroke="#aaa" fill="none"/></svg></div>
    <div class="arrow" style="left:1136px;top:331px"><svg width="8" height="10"><path d="M2 1l4 4-4 4" stroke="#333" fill="none"/></svg></div>
    <div class="outline-btn">View More</div>
  </section>

  <section class="about">
    <h2 class="section-title" style="top:1398px"><span class="accent">About</span> Us</h2>
    <p class="about-text">Lorem ipsum dolor sit amet, consectetur adipiscing elit, sed do eiusmod tempor incididunt ut labore et dolore magna aliqua. Ut enim ad minim veniam, quis nostrud exercitation ullamco laboris nisi ut aliquip ex ea commodo consequat. Duis aute irure dolor in reprehenderit in voluptate velit esse cillum dolore eu fugiat nulla pariatur. Excepteur sint occaecat cupidatat non proident, sunt in culpa qui officia deserunt mollit anim id est laborum.</p>
    <h3 class="about-head">Your Ridgeview Homefinder and its<br>unique value proposition</h3>
    <ul class="values">
      <li>Lorem ipsum dolor sit amet, consectetur</li>
      <li>Excepteur sint occaecat cupidatat non proident</li>
      <li>Duis aute irure dolor in reprehenderit</li>
      <li>Sed ut perspiciatis unde omnis iste natus error sit voluptatem accusantium doloremque laudantium.</li>
      <li>Lorem ipsum dolor sit amet, consectetur</li>
    </ul>
    <div class="btn" style="left:100px;top:1985px;width:134px;height:46px;font-size:16px">View More</div>
    <div class="about-art" role="img" aria-label="Illustrated hub of real estate service icons around the brand centre"></div>
  </section>

  <section class="testi">
    <h2 class="section-title" style="top:68px"><span class="accent">Client</span> Testimonials</h2>
    <div class="card t-card" style="left:96px"><div class="stars">★★★★★</div><p>Lorem ipsum dolor sit amet, consectetur adipiscing elit, sed do eiusmod tempor incididunt ut labore et dolore magna aliqua ut enim ad minim veniam, quis nostrud exercitation ullamco.</p><hr><div class="person"><div class="avatar" role="img" aria-label="Client portrait"></div><div><b>Mara Ellison</b><span>Florida, United States</span></div></div></div>
    <div class="card t-card" style="left:443px"><div class="stars">★★★★★</div><p>Lorem ipsum dolor sit amet, consectetur adipiscing elit, sed do eiusmod tempor incididunt ut labore et dolore magna aliqua ut enim ad minim veniam, quis nostrud exercitation ullamco.</p><hr><div class="person"><div class="avatar" role="img" aria-label="Client portrait"></div><div><b>Mara Ellison</b><span>Florida, United States</span></div></div></div>
    <div class="card t-card" style="left:791px"><div class="stars">★★★★★</div><p>Lorem ipsum dolor sit amet, consectetur adipiscing elit, sed do eiusmod tempor incididunt ut labore et dolore magna aliqua ut enim ad minim veniam, quis nostrud exercitation ullamco.</p><hr><div class="person"><div class="avatar" role="img" aria-label="Client portrait"></div><div><b>Mara Ellison</b><span>Florida, United States</span></div></div></div>
    <div class="arrow" style="left:40px;top:303px;border-color:#aaa"><svg width="8" height="10"><path d="M6 1L2 5l4 4" stroke="#aaa" fill="none"/></svg></div>
    <div class="arrow" style="left:1134px;top:303px"><svg width="8" height="10"><path d="M2 1l4 4-4 4" stroke="#333" fill="none"/></svg></div>
  </section>

  <section class="contact">
    <h2 class="section-title" style="top:2788px"><span class="accent">Contact</span> Us</h2>
    <div class="step-line" style="left:313px;width:288px"></div>
    <div class="step-line" style="left:661px;width:226px"></div>
    <div class="step out" style="left:253px">1</div>
    <div class="step fill" style="left:601px">2</div>
    <div class="step fill" style="left:887px">3</div>

    <div class="field full" style="top:2990px">Business Name:</div>
    <div class="field l" style="top:3060px">First Name:*</div><div class="field r" style="top:3060px">Last Name:*</div>
    <div class="field l" style="top:3132px">Email:*</div><div class="field r" style="top:3132px">Phone Number:*</div>
    <div class="divider" style="top:3222px"></div>
    <div class="field l" style="top:3255px">Realtor Name:*</div><div class="field r" style="top:3255px">Date and Time:*</div>
    <div class="field l" style="top:3327px">Venue/Location:*</div><div class="field r" style="top:3327px">Type of Realtor (Lorem ipsum dolor sit amet, etc.)</div>
    <div class="divider" style="top:3400px"></div>
    <div class="field l" style="top:3438px">Expected Size:*</div><div class="field r" style="top:3438px">Audience Profile (industry, background, level of expertise)</div>
    <div class="field l" style="top:3510px">Topic or Title of Presentation:</div><div class="field r" style="top:3510px">Desired Length of Presentation:</div>
    <div class="q">What format do you prefer for this speaking engagement?*</div>
    <div class="radios"><label><i></i>In Person</label><label><i></i>Virtual</label><label><i></i>Pre-Recorded</label></div>
    <div class="divider" style="top:3668px"></div>
    <div class="field" style="left:160px;width:878px;top:3700px">What is your budget?*</div>
    <div class="field" style="left:160px;width:878px;top:3768px;height:94px">Are there opportunities for book signings or other promotional activities?*</div>
    <div class="field" style="left:160px;width:878px;top:3880px">Additional Comments or Requests:*</div>
    <div class="btn" style="left:530px;top:3962px;width:138px;height:41px;font-size:16px">Submit</div>
  </section>

  <footer class="footer">
    <div class="brand" style="left:100px;top:60px"><span class="brand-dot"></span><span class="brand-name" style="color:#fff">Ridgeview<br><span class="accent" style="font-size:16px;letter-spacing:4px">Homefinder</span></span></div>
    <div class="f-social" aria-label="Social links"><span></span><span></span><span></span></div>
    <h4 style="left:380px;top:80px">Quick links</h4>
    <ul class="f-list" style="left:380px;top:130px"><li>Home</li><li>About Us</li><li>How it Works</li><li>Blog</li><li>Contact Us</li></ul>
    <h4 style="left:569px;top:78px">Contact us</h4>
    <div class="f-small" style="left:569px;top:128px;width:230px">Address<br>⌖ Lorem ipsum dolor sit amet, consectetur<br><br>Phone<br>✆ +1 555 010 7788<br><br>Email<br>✉ hello@ridgeviewhome.com</div>
    <h4 style="left:855px;top:78px">Newsletter</h4>
    <div class="f-small" style="left:855px;top:128px;width:240px;font-size:13.5px">Lorem ipsum dolor sit amet, consec tetur adipiscing elit, sed do</div>
    <div class="email-box">Email<span></span></div>
    <div class="copy">Copyrights 2024 Company Name | All Rights Reserved</div>
  </footer>

</div>
</body>
</html>
```